Design some Business Cards for Ena Fosk

I am looking for a sleek business card design. We are a software development firm, so the cards need to look cutting edge, minimalist, not cluttered, and catchy. I'd like the back to have our company name and a slogan. The company name is "Ena Fosk" with the umlaut over the "U" and the dot of the "i" even with that umlaut (see our temporary website at [url removed, login to view]). The slogan is "Software development done right." Our website uses orange, which is fine. But feel free to experiment with other colors (maybe blue?).

Also, the font for the company name is Google's Comfortaa.

The front will have the usual data: name, email, phone number, website. No address.

Thanks to all who submit.

```html
<!DOCTYPE html>
<html lang="en">
<head>
<meta charset="utf-8">
<title>Ena Fosk — Business Card</title>
<link href="https://fonts.googleapis.com/css2?family=Comfortaa:wght@300&family=Poppins:wght@500;600&display=swap" rel="stylesheet">
<style>
  :root {
    --ink: #2f3739;
    --ink-soft: #3d4749;
    --flame: #dd4a2b;
    --sun: #f0b65a;
    --paper: #ffffff;
  }
  html, body {
    margin: 0;
    padding: 0;
    width: 1200px;
    height: 701px;
    overflow: hidden;
    background: var(--paper);
  }
  .card {
    display: block;
    width: 1200px;
    height: 701px;
  }
  .ink { fill: var(--ink); }
  .flame { fill: var(--flame); }
  .paper { fill: var(--paper); }
  .brand-disc {
    fill: var(--flame);
    stroke: var(--paper);
    stroke-width: 10;
  }
  .holder-name {
    font-family: "Poppins", sans-serif;
    font-weight: 600;
    font-size: 22px;
    fill: var(--paper);
    letter-spacing: 0.3px;
  }
  .holder-email {
    font-family: "Poppins", sans-serif;
    font-weight: 500;
    font-size: 21px;
    fill: var(--paper);
  }
  .brand-name {
    font-family: "Comfortaa", sans-serif;
    font-weight: 300;
    font-size: 68px;
    fill: var(--paper);
  }
  .contact-phone {
    font-family: "Poppins", sans-serif;
    font-weight: 600;
    font-size: 24px;
    fill: var(--flame);
    letter-spacing: 1px;
  }
  .contact-web {
    font-family: "Poppins", sans-serif;
    font-weight: 500;
    font-size: 17px;
    fill: var(--flame);
  }
  .icon-line {
    fill: none;
    stroke: var(--paper);
    stroke-width: 1.6;
  }
</style>
</head>
<body>
<svg class="card" viewBox="0 0 900 526" xmlns="http://www.w3.org/2000/svg">
  <defs>
    <linearGradient id="decor-fill" x1="0" y1="0" x2="1" y2="1">
      <stop offset="0" stop-color="var(--ink-soft)"/>
      <stop offset="1" stop-color="var(--ink)"/>
    </linearGradient>
  </defs>

  <!-- top information band -->
  <rect class="ink" x="0" y="58" width="460" height="110"/>

  <!-- lower decorative field -->
  <rect x="0" y="168" width="900" height="358" fill="url(#decor-fill)" role="img" aria-label="Dark diagonal stripe decoration"/>

  <!-- contact panel -->
  <polygon class="paper" points="206,368 470,368 600,495 148,495"/>

  <!-- brand disc -->
  <circle class="brand-disc" cx="702" cy="150" r="215"/>
  <text class="brand-name" x="702" y="172" text-anchor="middle">Ena Fosk</text>

  <!-- card holder -->
  <text class="holder-name" x="25" y="97">NAME.................</text>
  <text class="holder-email" x="25" y="131">Example@example.com</text>

  <!-- phone -->
  <g class="phone-icon" transform="translate(204,376)">
    <rect class="flame" x="0" y="8" width="44" height="36" rx="5"/>
    <path class="flame" d="M2,12 C2,0 42,0 42,12 L34,12 C34,6 10,6 10,12 Z"/>
    <rect class="paper" x="14" y="16" width="24" height="22" rx="2"/>
    <g class="flame">
      <rect x="17" y="19" width="4" height="4"/>
      <rect x="24" y="19" width="4" height="4"/>
      <rect x="31" y="19" width="4" height="4"/>
      <rect x="17" y="25" width="4" height="4"/>
      <rect x="24" y="25" width="4" height="4"/>
      <rect x="31" y="25" width="4" height="4"/>
      <rect x="17" y="31" width="4" height="4"/>
      <rect x="24" y="31" width="4" height="4"/>
      <rect x="31" y="31" width="4" height="4"/>
    </g>
    <rect class="paper" x="4" y="14" width="6" height="26" rx="3"/>
  </g>
  <text class="contact-phone" x="262" y="408">1234567890</text>

  <!-- website -->
  <g class="web-icon" transform="translate(176,460)">
    <circle class="flame" cx="0" cy="0" r="23"/>
    <ellipse class="icon-line" cx="0" cy="0" rx="10" ry="20"/>
    <line class="icon-line" x1="-20" y1="0" x2="20" y2="0"/>
    <line class="icon-line" x1="-17" y1="-10" x2="17" y2="-10"/>
    <line class="icon-line" x1="-17" y1="10" x2="17" y2="10"/>
  </g>
  <text class="contact-web" x="213" y="466">Example.com</text>
</svg>
</body>
</html>
```